Business card and company stationary - Corvane Cleaning Ltd

1. Who are we and who are our customers?

o We are a relatively new cleaning company, established December 2008. We are a small company. We have 24 staff and we offer domestic and commercial cleaning services.
o We both (me and my wife) have been working for many years in the cleaning industry. We worked for some of the biggest and best cleaning companies in UK. We’ve been operatives, supervisors and managers.
o Inevitably after so many years of working for someone else, we decided to start our own business.
o Our domestic customers are middle class families and busy professionals. We’ve got some commercial customers, mainly offices.
o We are growing steadily.

2. What do we do? What are our services?

o Cleaning. We’ve got range of services - not to many but still can be daunting and confusing for some.
o Generally we’ve got domestic and commercial clients. The approach to the domestic cleaning customers is different to the commercial. In the way we want to say that it is cleaning that we do, but we acknowledge the environment and we appreciate the personal circumstances and requirements that are present. We do care, we listen and we try to work out the best possible way to complete our work.
o Mainly we get our work through referrals

3. What do we want with our stationery ?

o To place and maintain our message and reach out to people and organisations
o We want to advertise, communicate and sale.
o We are going to sell services.
o Increase membership, loyalty and support.

We are after business card design, headed letter and compliment slip.
We would like the headed letter to be created in formats suitable for :
- printing format
- also for use in our daily correspondence via e mail with clients and staff in a easy to edit and write format

The website we have is still under contraction and the domain is corvanecleaning.example

Target Market(s)

Families, individuals, businesses.

Industry/Entity Type

Cleaning Service

Contact Information for Business Card

FRONT :
Company Name - Corvane Cleaning Ltd
Company address - 41 Pelbury Rd, Pelbury, Essex, RM14 7QT
Name - Mrs. Teodora Vasilkova - Tedi
Title - Managing Director
Company phone - 020 8837 2591
E mail - tedi.vasilkova@corvanecleaning.example

BACK :

Company website - corvanecleaning.example
E mail - enquiries@corvanecleaning.example

Font styles to use
Serif

Requirements
Must have
• The above items and company logo...maybe at the back. But I'm free for any suggestions.

```html
<!DOCTYPE html>
<html lang="en">
<head>
<meta charset="utf-8">
<title>Corvane Cleaning Ltd — Stationery</title>
<link rel="stylesheet" href="https://fonts.googleapis.com/css2?family=Signika:wght@400;600;700&family=Merriweather:wght@700&display=swap">
<style>
  :root {
    --bg: #dcdcda;
    --paper: #ffffff;
    --blue-deep: #0162b1;
    --blue-mid: #0a7fcf;
    --blue-sky: #00b6ee;
    --blue-pale: #52cdf5;
    --ink: #222831;
    --ring: #e9ecef;
  }
  * { box-sizing: border-box; margin: 0; padding: 0; }
  html, body { width: 1200px; height: 778px; overflow: hidden; }
  body { background: var(--bg); font-family: "Signika", Arial, sans-serif; color: var(--ink); position: relative; }

  .piece { position: absolute; background: var(--paper); box-shadow: 0 1px 3px rgba(0,0,0,.25); overflow: hidden; }
  .piece > svg.waves { position: absolute; inset: 0; width: 100%; height: 100%; }

  .brand { position: absolute; display: flex; flex-direction: column; align-items: center; text-align: center; z-index: 1; }
  .brand-mark { border-radius: 50%; border: 2px solid currentColor; }
  .brand-name { font-weight: 700; color: var(--blue-sky); line-height: 1.05; letter-spacing: .04em; text-transform: uppercase; }

  .contacts { position: absolute; font-size: 8px; font-weight: 600; line-height: 1.9; color: var(--ink); z-index: 1; }
  .contacts .row { display: flex; align-items: center; gap: 4px; white-space: nowrap; }
  .icon { width: 9px; height: 9px; flex: none; }

  /* business card front */
  .card-front { left: 114px; top: 102px; width: 243px; height: 150px; background: radial-gradient(circle at 50% 30%, #1896e2, var(--blue-deep) 85%); }
  .card-front .brand { left: 0; right: 0; top: 16px; color: #fff; }
  .card-front .brand-mark { width: 40px; height: 40px; margin-bottom: 5px; }
  .card-front .brand-name { color: #fff; font-size: 13px; }
  .card-front .tagline { position: absolute; left: 0; right: 0; top: 91px; text-align: center; font-family: "Merriweather", Georgia, serif; font-size: 8.5px; color: #fff; z-index: 1; }

  /* business card back */
  .card-back { left: 387px; top: 102px; width: 243px; height: 150px; }
  .card-back .brand { left: 14px; top: 14px; color: var(--blue-deep); }
  .card-back .brand-mark { width: 24px; height: 24px; margin-bottom: 3px; }
  .card-back .brand-name { font-size: 8px; }
  .card-back .person { position: absolute; right: 14px; top: 12px; text-align: right; }
  .card-back .person-name { font-family: "Merriweather", Georgia, serif; font-size: 11px; color: var(--blue-deep); }
  .card-back .person-role { font-size: 7px; font-weight: 600; }
  .card-back .contacts { right: 13px; top: 78px; font-size: 6.5px; line-height: 1.75; align-items: flex-end; display: flex; flex-direction: column; }
  .card-back .contacts .icon { width: 8px; height: 8px; }

  /* envelope */
  .envelope { left: 113px; top: 287px; width: 506px; height: 257px; border-radius: 26px 26px 0 0; }
  .envelope .flap { position: absolute; left: 0; top: 0; width: 100%; height: 37px; background: linear-gradient(90deg, var(--blue-sky), var(--blue-mid)); }
  .envelope .ghost-ring { position: absolute; left: 280px; top: 48px; width: 240px; height: 240px; border-radius: 50%; border: 18px solid var(--ring); opacity: .7; }
  .envelope .brand { left: 340px; top: 58px; color: var(--ink); }
  .envelope .brand-mark { width: 58px; height: 58px; margin-bottom: 6px; }
  .envelope .brand-name { font-size: 19px; }
  .envelope .contacts { left: 21px; top: 181px; }

  /* letterhead */
  .letterhead { left: 669px; top: 99px; width: 421px; height: 597px; }
  .letterhead .brand { left: 33px; top: 18px; color: var(--ink); }
  .letterhead .brand-mark { width: 42px; height: 42px; margin-bottom: 5px; }
  .letterhead .brand-name { font-size: 13px; }
  .letterhead .contacts { right: 20px; top: 531px; display: flex; flex-direction: column; align-items: flex-end; }
</style>
</head>
<body>

<svg width="0" height="0" style="position:absolute" aria-hidden="true">
  <defs>
    <symbol id="ico-phone" viewBox="0 0 10 10"><circle cx="5" cy="5" r="5" fill="#0a7fcf"/><path d="M3.2 2.6l1 1-.5.7c.3.7.8 1.2 1.5 1.5l.7-.5 1 1-.7.9C4.9 7 3 5.1 2.8 3.3z" fill="#fff"/></symbol>
    <symbol id="ico-fax" viewBox="0 0 10 10"><circle cx="5" cy="5" r="5" fill="#0a7fcf"/><rect x="3" y="2.6" width="4" height="4.8" rx=".6" fill="#fff"/></symbol>
    <symbol id="ico-mail" viewBox="0 0 10 10"><circle cx="5" cy="5" r="5" fill="#0a7fcf"/><rect x="2.5" y="3.3" width="5" height="3.4" fill="#fff"/><path d="M2.5 3.3L5 5.3l2.5-2" stroke="#0a7fcf" stroke-width=".6" fill="none"/></symbol>
    <symbol id="ico-web" viewBox="0 0 10 10"><circle cx="5" cy="5" r="5" fill="#0a7fcf"/><circle cx="5" cy="5" r="2.6" fill="none" stroke="#fff" stroke-width=".8"/><path d="M2.4 5h5.2M5 2.4v5.2" stroke="#fff" stroke-width=".6"/></symbol>
    <symbol id="ico-pin" viewBox="0 0 10 10"><circle cx="5" cy="5" r="5" fill="#0a7fcf"/><path d="M5 8L3.2 5.2A2 2 0 1 1 6.8 5.2z" fill="#fff"/></symbol>
  </defs>
</svg>

<!-- Business card: front -->
<section class="piece card-front" aria-label="Business card front">
  <svg class="waves" viewBox="0 0 243 150" preserveAspectRatio="none" aria-hidden="true">
    <path d="M0 136C70 126 160 128 243 106V150H0z" fill="#0150a0"/>
    <path d="M0 134C80 122 160 126 243 104" stroke="#52cdf5" stroke-width="2" fill="none"/>
    <path d="M0 142C80 130 170 132 243 112" stroke="#52cdf5" stroke-width="1.2" fill="none" opacity=".7"/>
  </svg>
  <div class="brand">
    <span class="brand-mark"></span>
    <span class="brand-name">Corvane<br>Cleaning Ltd</span>
  </div>
  <p class="tagline">cleaning • housekeeping • support services</p>
</section>

<!-- Business card: back -->
<section class="piece card-back" aria-label="Business card back">
  <svg class="waves" viewBox="0 0 243 150" preserveAspectRatio="none" aria-hidden="true">
    <g transform="translate(0 8)">
      <path d="M0 62C70 70 150 30 243 40V62C170 54 120 70 60 110C40 122 20 124 0 122z" fill="#0a7fcf"/>
      <path d="M0 58C70 66 150 26 243 36V42C150 34 80 74 0 64z" fill="#52cdf5"/>
      <path d="M0 70C80 76 150 42 243 48" stroke="#52cdf5" stroke-width="1.4" fill="none"/>
    </g>
  </svg>
  <div class="brand">
    <span class="brand-mark"></span>
    <span class="brand-name">Corvane<br>Cleaning Ltd</span>
  </div>
  <div class="person">
    <p class="person-name">Owner Name</p>
    <p class="person-role">President</p>
  </div>
  <div class="contacts">
    <p class="row"><svg class="icon"><use href="#ico-phone"/></svg>(+880) 555-014</p>
    <p class="row"><svg class="icon"><use href="#ico-fax"/></svg>(+130) 555-027</p>
    <p class="row"><svg class="icon"><use href="#ico-mail"/></svg>hello@corvanecleaning.example</p>
    <p class="row"><svg class="icon"><use href="#ico-web"/></svg>www.corvanecleaning.example</p>
    <p class="row"><svg class="icon"><use href="#ico-pin"/></svg>Please provide full address of your company</p>
  </div>
</section>

<!-- Envelope -->
<section class="piece envelope" aria-label="Envelope">
  <div class="flap"></div>
  <div class="ghost-ring" aria-hidden="true"></div>
  <svg class="waves" viewBox="0 0 506 257" preserveAspectRatio="none" aria-hidden="true">
    <defs>
      <linearGradient id="env-grad" x1="0" y1="0" x2="1" y2="1">
        <stop offset="0" stop-color="#00b6ee"/><stop offset="1" stop-color="#0162b1"/>
      </linearGradient>
    </defs>
    <path d="M0 37H20C140 40 240 120 330 160C400 190 460 190 506 186V232C420 226 300 190 210 160C120 132 60 128 0 140z" fill="url(#env-grad)"/>
    <path d="M0 137C80 122 150 138 240 170C330 200 420 226 506 228" stroke="#52cdf5" stroke-width="5" fill="none"/>
    <path d="M0 146C90 134 170 152 250 178C340 208 430 236 506 240" stroke="#52cdf5" stroke-width="2" fill="none"/>
  </svg>
  <div class="brand">
    <span class="brand-mark"></span>
    <span class="brand-name">Corvane<br>Cleaning Ltd</span>
  </div>
  <div class="contacts">
    <p class="row"><svg class="icon"><use href="#ico-phone"/></svg>(+880) 555-014 <svg class="icon"><use href="#ico-fax"/></svg>(+130) 555-027</p>
    <p class="row"><svg class="icon"><use href="#ico-mail"/></svg>hello@corvanecleaning.example <svg class="icon"><use href="#ico-web"/></svg>www.corvanecleaning.example</p>
    <p class="row"><svg class="icon"><use href="#ico-pin"/></svg>Please provide full address of your company</p>
  </div>
</section>

<!-- Letterhead -->
<section class="piece letterhead" aria-label="Letterhead">
  <svg class="waves" viewBox="0 0 421 597" preserveAspectRatio="none" aria-hidden="true">
    <defs>
      <linearGradient id="lh-grad" x1="0" y1="1" x2="1" y2="0">
        <stop offset="0" stop-color="#0162b1"/><stop offset="1" stop-color="#00b6ee"/>
      </linearGradient>
    </defs>
    <path d="M0 106C90 112 170 70 270 36C335 16 385 9 421 6V88C330 92 220 112 120 130C70 140 30 142 0 138z" fill="url(#lh-grad)"/>
    <path d="M0 138C60 144 140 130 240 110C320 96 380 90 421 88" stroke="#52cdf5" stroke-width="5" fill="none"/>
    <path d="M0 148C70 152 150 138 250 120C330 106 385 100 421 98" stroke="#52cdf5" stroke-width="2" fill="none"/>
    <path d="M0 481C60 488 130 520 230 597H0z" fill="url(#lh-grad)"/>
    <path d="M0 558C60 556 120 570 180 597" stroke="#52cdf5" stroke-width="3" fill="none"/>
  </svg>
  <div class="brand">
    <span class="brand-mark"></span>
    <span class="brand-name">Corvane<br>Cleaning Ltd</span>
  </div>
  <div class="contacts">
    <p class="row"><svg class="icon"><use href="#ico-phone"/></svg>(+880) 555-014 <svg class="icon"><use href="#ico-fax"/></svg>(+130) 555-027</p>
    <p class="row"><svg class="icon"><use href="#ico-mail"/></svg>hello@corvanecleaning.example <svg class="icon"><use href="#ico-web"/></svg>www.corvanecleaning.example</p>
    <p class="row"><svg class="icon"><use href="#ico-pin"/></svg>Please provide full address of your company</p>
  </div>
</section>

</body>
</html>
```